Postcard: Open Sky Circle

Text for front: HOW TO CHANGE THE WORLD IN ONE [note: the word "one" should be underlined] STEPHint: It's up to you...[Note: add arrow or something to indicate "turn over"]Text for back: You're going to spend your entire life with someone you can never get away from. (Guess who?) Wouldn't you rather that person #OpenSkyCircle than judgmental or critical? BE the change you want to see! Visit www.OpenSkyCircle-hub.example for daily Dawn Pebbles and community. PLEASE JOIN US![Note: add logo to left half of back side]Font preference for text: Josefin sans

Target Market(s)

People who would be attracted to Corvane church - teravian perennist message. It's spiritual without being overtly religious, so the target market is probably early 30s and up but ideally won't turn off Millennials (folks under 30). It should attract attention of people who are open-minded and committed to progressive social change, tired of an atmosphere of hate-mongering and divisiveness.

Requirements
Nice to have
• It would be nice to convey a sense of challenge - there is an idea of "dawn pebbles" so something related to fire/sparks is appropriate. This is meant to evoke a deeper, divine love more than a sense of romantic love. This love is more fierce than fluffy! Yet it calls us to be our best selves.
Should not have
• Please avoid excessive pink - just the logo is enough, as this design needs to appeal to men as well as women.

```html
<!DOCTYPE html>
<html lang="en">
<head>
<meta charset="utf-8">
<title>Open Sky Circle Postcard</title>
<link rel="stylesheet" href="https://fonts.googleapis.com/css2?family=Josefin+Sans:wght@300;400&family=Great+Vibes&display=swap">
<style>
  :root {
    --page-bg: #e9e7e3;
    --card-bg: #f6f3ea;
    --card-edge: #e4dfd2;
    --rose: #e8508e;
    --rose-deep: #e0317a;
    --rose-soft: #f29ab9;
    --peach: #f6d2b8;
    --ink: #4a4744;
    --arrow-grey: #b9b7b3;
    --white: #ffffff;
  }
  * { margin: 0; padding: 0; box-sizing: border-box; }
  html, body {
    width: 933px;
    height: 1200px;
    overflow: hidden;
    background: var(--page-bg);
  }
  .canvas {
    position: relative;
    width: 933px;
    height: 1200px;
  }
  .postcard {
    position: absolute;
    left: 110px;
    width: 710px;
    height: 483px;
    background: var(--card-bg);
    border: 1px solid var(--card-edge);
    overflow: hidden;
  }
  .postcard--front { top: 99px; }
  .postcard--back { top: 630px; }

  .wash {
    position: absolute;
    left: 0; top: 0;
    width: 100%;
    height: 300px;
    background:
      radial-gradient(ellipse 60% 70% at 30% 20%, var(--rose-deep) 0%, transparent 70%),
      radial-gradient(ellipse 50% 60% at 80% 40%, var(--rose) 0%, transparent 75%),
      linear-gradient(180deg, var(--rose) 0%, var(--rose-soft) 55%, var(--peach) 80%, rgba(246,243,234,0) 100%);
  }
  .headline {
    position: absolute;
    left: 0; top: 34px;
    width: 100%;
    text-align: center;
    font-family: "Josefin Sans", sans-serif;
    font-weight: 300;
    font-size: 53px;
    line-height: 73px;
    letter-spacing: 1px;
    color: var(--white);
  }
  .headline u {
    text-decoration-thickness: 2px;
    text-underline-offset: 8px;
  }
  .hint {
    position: absolute;
    left: 52px; top: 384px;
    font-family: "Great Vibes", cursive;
    font-size: 36px;
    color: var(--rose);
  }
  .turn-arrow {
    position: absolute;
    left: 455px; top: 338px;
    width: 220px;
    height: 100px;
  }

  .brand {
    position: absolute;
    left: 43px; top: 60px;
    width: 330px;
    height: 290px;
    display: flex;
    align-items: center;
    justify-content: center;
    gap: 14px;
  }
  .brand__dot {
    width: 22px; height: 22px;
    border-radius: 50%;
    background: var(--rose);
  }
  .brand__name {
    font-family: "Josefin Sans", sans-serif;
    font-weight: 300;
    font-size: 34px;
    color: var(--rose);
  }
  .message {
    position: absolute;
    left: 375px; top: 54px;
    width: 310px;
    text-align: center;
    font-family: "Josefin Sans", sans-serif;
    font-weight: 300;
    font-size: 15.5px;
    line-height: 19px;
    color: var(--ink);
  }
  .message p + p { margin-top: 19px; }
  .message .link { color: var(--rose); }
  .join {
    position: absolute;
    left: 0; top: 378px;
    width: 100%;
    text-align: center;
    font-family: "Josefin Sans", sans-serif;
    font-weight: 300;
    font-size: 58px;
    letter-spacing: 2px;
    color: var(--rose);
  }
</style>
</head>
<body>
<main class="canvas">
  <section class="postcard postcard--front">
    <div class="wash" role="img" aria-label="Soft pink and peach watercolour wash"></div>
    <h1 class="headline">HOW TO CHANGE<br>THE WORLD<br>IN <u>ONE</u> STEP</h1>
    <p class="hint">Hint: It's up to you...</p>
    <svg class="turn-arrow" viewBox="0 0 220 100" aria-hidden="true">
      <path d="M6 52 C40 30 80 24 150 40 L146 18 L212 62 L140 88 L146 66 C90 54 50 60 14 78 Z"
            fill="none" stroke="var(--arrow-grey)" stroke-width="3" stroke-linejoin="round"/>
    </svg>
  </section>

  <section class="postcard postcard--back">
    <div class="brand">
      <span class="brand__dot"></span>
      <span class="brand__name">Open Sky Circle</span>
    </div>
    <div class="message">
      <p>You're going to spend your entire life with someone you can never get away from. (Guess who?)</p>
      <p>Wouldn't you rather that person #OpenSkyCircle than judgmental or critical?</p>
      <p>BE the change you want to see! Visit <span class="link">www.OpenSkyCircle-hub.example</span> for daily Dawn Pebbles and community.</p>
    </div>
    <p class="join">PLEASE JOIN US!</p>
  </section>
</main>
</body>
</html>
```